Web Design for Solar Energy Consultancy Company

~ May 3, 2017 Update ~
As our project is rapidly progressing towards its completion, we started building up the list of designs that attracted the most of the team's attention. Additional submittals are still most welcome. Before submitting your proposal, however, we can recommend to review the concepts that received 4 stars as these are the ones that, in our opinion, most closely match the brief's requirements. Thank you!!
~ April 30, 2017 Update ~
The project deadline has been extended to attract a broader design community and to better tailor the final design to the requirements of the project.
A "light", "clean" (minimalistic), professionally looking, unique design is expected. Please, try to avoid industry cliches. Also, please use green, which became another industry cliche, with great caution. The brief provides minimum details to foster creativity. With the same notion in mind, the page content information is not provided.
Thank you for your feedback and support of the project!!
~ April 22, 2017 Update ~
Additional comments after starting receiving more designs:
- your attention to the brief's requirements will be highly appreciated. It is expected that the design is unique - standard, commonly used, images, formats and approaches do not fall under this category. There is no need to "bombard" with slightly different variations of the same design. It is expected that a conceptual (preliminary) design is submitted first, and, after it is reviewed (each design will receive a star rating and, if the star rating is greater than 3, a detailed feedback), the requested changes are implemented. We believe this will allow to approach the design process more efficiently and safe additional time to both the Designers's Community and our company. Thank you for understanding.
Clarification, please submit two variations of a design:
1) 1 page "business card" design that the company will be able to use during its startup stage;
2) the fully functional design (as per the requirements outlined below) for the company to transition to after the start-up period is over. Same design principles as developed for option 1 should be used for this variation.
Additional clarification, please note that the news block will not require images (at least during the start-up stage). It is envisioned to be a news feeder.
~ April 21, 2017 Update ~
Preliminary comments after receiving first designs:
- please try to create a unique design, using common elements wisely. Though such solar energy "attributes" as a solar panel or a bulb are very well recognized and allow quickly identify the nature of the business, they also became so common that in many cases a design may seem very similar to the one of others (Oh!, I've already seen this... effect).
- please try to introduce the company's logo unobtrusively. The size and position of the logo should clearly identify the company, but the message should be subtle, the logo should not distract from the main design. Brask's swoosh did not need to occupy have the screen.
- please use the green color with caution as it was with the company's logo. True, it is a green energy. But there is no need for the color to "scream" about it. Use the amount of green and its tone (avoid acid green) wisely.
--------------------------------------------------------------------------------
1. Main Goal
Develop a website that can represent the company to the industry stakeholders and become its "business card" during the start-up stage.
2. Secondary Goal
Develop a structure of a fully functional website that the "business card" design can eventually be transformed to staying consistent with the original design principles.
3. Key Audience
Varolu Corp. is providing consulting and technical services in the area of Solar Energy. The industry stakeholders include project developers, financial community, governmental bodies, OEMs, and competition.
4. Site Map
- HOME
• About
• Services
• Solar Energy
• News
• Contacts
• Social Media
- SERVICES*
- PROJECTS*
- FINANCE*
- TRAINING*
- SOLAR (ENERGY)*
* Maybe inactive / partially functional during the start-up stage.
5. Technical Specifications
Online brochure website during the start-up stage with a capability to be eventually transformed to a fully functional website while preserving the original design principles.
The design to be appealing, "light", professional, and with an intuitive and easy to navigate interface. Modern coding principles supporting efficiency and security to be utilized. Newest industry trends in website coding will be welcome.
The website to be designed so that it would fit well a computer, tablet, or mobile phone screen of any size. Cross-platform functionality to be taken into consideration to ensure that the website is fully functional on any platform.
Company's logo has already been designed and will be shared with the short-listed designers during the final design stage.
6. Interaction
The website will provide information about the company, our services, and projects. In addition, the industry insight, accumulated knowledge, and most recent trends are planned to be shared with stakeholders and attract and retain the audience.
Interaction with designers during the website development is envisioned to go through the following steps:
a) conceptual design - to be proposed by a designer originally. All conceptual designs will be reviewed and a feedback provided to pre-selected designers;
b) (preliminary and) final design - depending on the level of additional changes required can be broken into two steps. After discussing preliminary designs, company images will be provided to the selected finalists, who will compete with their final proposals.
7. Industry Stakeholders
- https://www.quellbrin.com/power/solar-power.- http://www.pakortavon.com/
- http://www.vellitrazo.com/about/company/
- https://www.oruxem.com/energy/index.html
8. Budget
Defined by the project.
9. Timescale
Defined by the project.
12. Additional Info
- No copy-cats, standard graphics, or cliches please!
- Additional information / clarifications will be gladly provided upon request.
- This specification may be updated throughout the project to reflect discussions with / changes proposed by the Designers community.

```html
<!DOCTYPE html>
<html lang="en">
<head>
<meta charset="utf-8">
<title>Varolu Corp. — Solar Energy Consulting</title>
<link rel="stylesheet" href="https://fonts.googleapis.com/css2?family=Jura:wght@600;700&family=Open+Sans:wght@400;600;700&display=swap">
<style>
  :root {
    --ink: #2b2b2b;
    --text: #444;
    --rule: #9a9a9a;
    --accent: #f0a30a;
    --brand-green: #1e8f3a;
    --band-1: #78c850;
    --band-2: #8fd466;
    --band-3: #a5dc7f;
    --sky-top: #f4f4f4;
    --sky-bottom: #dedede;
    --visual-light: #e2d48a;
    --visual-deep: #cbbd63;
    --white: #ffffff;
  }
  * { margin: 0; padding: 0; box-sizing: border-box; }
  html, body { width: 1200px; height: 576px; overflow: hidden; }
  body {
    position: relative;
    font-family: "Open Sans", Arial, sans-serif;
    color: var(--text);
    background: var(--sky-top);
  }
  .hero-backdrop {
    position: absolute; left: 0; top: 0; width: 1200px; height: 425px;
    background: linear-gradient(180deg, var(--sky-top) 0%, #ebebeb 55%, var(--sky-bottom) 100%);
  }
  .brand {
    position: absolute; left: 182px; top: 15px;
    display: flex; align-items: center; gap: 10px;
  }
  .brand-dot { width: 42px; height: 42px; border-radius: 50%; background: var(--accent); }
  .brand-name {
    font-family: "Jura", Arial, sans-serif; font-weight: 700;
    font-size: 22px; color: #4a4a4a;
  }
  .top-actions {
    position: absolute; left: 845px; top: 21px;
    display: flex; gap: 5px; align-items: center;
  }
  .social-link {
    width: 24px; height: 24px; border: 1px solid #555; background: var(--white);
  }
  .contact-button {
    margin-left: 5px; height: 24px; width: 89px;
    background: var(--accent); color: var(--white);
    font-size: 11px; font-weight: 700; letter-spacing: 0.4px;
    display: flex; align-items: center; justify-content: center;
  }
  .headline {
    position: absolute; left: 216px; top: 101px;
    font-family: "Jura", Arial, sans-serif; font-weight: 700;
    font-size: 24px; letter-spacing: 0.2px; color: var(--brand-green);
    -webkit-text-stroke: 0.6px var(--brand-green);
  }
  .tagline {
    position: absolute; right: 624px; top: 130px;
    font-size: 13px; color: var(--ink);
  }
  .hero-visual {
    position: absolute; left: 240px; top: 178px; width: 325px; height: 194px;
    border-radius: 110px 60px 60px 110px;
    background: radial-gradient(circle at 35% 40%, var(--visual-light) 0%, var(--visual-deep) 100%);
  }
  .info-block { position: absolute; left: 609px; width: 414px; }
  .info-title {
    font-family: "Jura", Arial, sans-serif; font-weight: 700;
    font-size: 16px; color: var(--ink);
    -webkit-text-stroke: 0.4px var(--ink);
    padding-bottom: 11px; border-bottom: 1px solid var(--rule); position: relative;
  }
  .info-title::after {
    content: ""; position: absolute; left: 0; bottom: -2px;
    width: 29px; height: 3px; background: var(--accent);
  }
  .solar-energy { top: 142px; }
  .solar-energy p {
    margin: 21px 0 0 5px; width: 400px;
    font-size: 11.4px; line-height: 17px; color: var(--text);
  }
  .services { top: 280px; }
  .service-list {
    list-style: none; margin-top: 20px;
    display: grid; grid-template-columns: 222px 192px; row-gap: 10px;
  }
  .service-list li {
    font-size: 13px; font-weight: 700; color: var(--ink);
    padding-left: 20px; position: relative; line-height: 18px;
  }
  .service-list li::before {
    content: ""; position: absolute; left: 1px; top: 7px;
    width: 5px; height: 5px; border-radius: 50%; background: var(--brand-green);
  }
  .feature-bands {
    position: absolute; left: 0; top: 425px; width: 1200px; height: 151px;
    display: flex;
  }
  .feature { width: 400px; text-align: center; color: var(--white); padding-top: 35px; }
  .feature.projects { background: var(--band-1); }
  .feature.finance { background: var(--band-2); }
  .feature.training { background: var(--band-3); }
  .feature h2 {
    font-family: "Jura", Arial, sans-serif; font-weight: 700;
    font-size: 15px; letter-spacing: 0.6px;
    -webkit-text-stroke: 0.4px var(--white);
  }
  .feature p {
    width: 290px; margin: 21px auto 0;
    font-size: 11.3px; line-height: 17px;
  }
</style>
</head>
<body>
  <div class="hero-backdrop" role="img" aria-label="Faded grey photograph of a city skyline with high-rise towers"></div>

  <header>
    <div class="brand">
      <span class="brand-dot"></span>
      <span class="brand-name">Varolu Corp.</span>
    </div>
    <nav class="top-actions">
      <span class="social-link" aria-label="Social profile"></span>
      <span class="social-link" aria-label="Social profile"></span>
      <span class="social-link" aria-label="Social profile"></span>
      <span class="contact-button">CONTACT US</span>
    </nav>
  </header>

  <h1 class="headline">SHOULDER RESPONSIBILITY</h1>
  <p class="tagline">Join hands with us to better your living</p>

  <div class="hero-visual" role="img" aria-label="Photograph of a light bulb holding a sunlit landscape"></div>

  <section class="info-block solar-energy">
    <h2 class="info-title">Solar Energy</h2>
    <p>Lorem ipsum dolor sit amet, consectetur adipiscing elit, sed do eiusmod tempor incididunt ut labore et dolore magna aliqua. Ut enim ad minim veniam, congue nihil imperdiet doming id quod mazim placerat facer possim assum. Typi non habent claritatem insitam</p>
  </section>

  <section class="info-block services">
    <h2 class="info-title">Services</h2>
    <ul class="service-list">
      <li>Market Intelligence</li>
      <li>Analytical Solar Consulting</li>
      <li>Solar Design &amp; Engineering</li>
      <li>Technical Support</li>
    </ul>
  </section>

  <section class="feature-bands">
    <article class="feature projects">
      <h2>PROJECTS</h2>
      <p>Duis aute irure dolor in reprehenderit in volupt ate velit esse cillum dolore eu fugiat nulla tutur Excepteur sint occaec. vel eum iriure dolor</p>
    </article>
    <article class="feature finance">
      <h2>FINANCE</h2>
      <p>Typi non habent claritatem insitam; est usus lege ntis in iis qui facit eorum claritatem. Investigationes demonstraverunt lectores legere me</p>
    </article>
    <article class="feature training">
      <h2>TRAINING</h2>
      <p>Mirum est notare quam littera gothica, quam nunc putamus parum claram, anteposuerit litterarum formas humanitatis</p>
    </article>
  </section>
</body>
</html>
```